Local Service Business Needing Clear Business Card Design

We are needing a business card design to be made for our power washing company. Business cards will be printed on plastic standard sized cards. We're looking for someone who can make a unique and unforgettable design. Double sided and or single sided concepts would be ideal. Of course keeping in mind we are seeking translucent cards but not married to the idea of having them as the main concern is just to have plastic cards to prevent water damage! :D

More info on our company can be found on lakeshorebrightwash.example

Not looking for a list of our services. Simply applying company info and possibly "Commercial Residential Fleet" on them tastefully and appropriate to design is all thats needed.

Phone number for our company is 855-GLO-TEAM or 855-456-8326

Industry/Entity Type

Power Washing

Contact Information for Business Card

Phone, Web URL,

Requirements
Should not have
• Bubbles, water or super distracting graphics. Looking for a simple and clean look. Unfortunately our logo is this way which we may seek to change in the near future.

```html
<!DOCTYPE html>
<html lang="en">
<head>
<meta charset="utf-8">
<title>Lakeshore Bright Wash – Business Card</title>
<link rel="stylesheet" href="https://fonts.googleapis.com/css2?family=Roboto:wght@400;500;700;900&display=swap">
<style>
  :root {
    --page-bg: #e9e7e4;
    --card-frost: #f1f2f3;
    --card-edge: #d4d8dc;
    --panel-blue: #0d4a9c;
    --panel-deep: #083679;
    --panel-accent: #2f7fd0;
    --name-blue: #1c6fa3;
    --call-light: #2aa3d8;
    --call-navy: #0f3b78;
    --text-dark: #2b2f36;
    --icon-blue: #2aa3d8;
    --white: #ffffff;
  }
  * { margin: 0; padding: 0; box-sizing: border-box; }
  html, body {
    width: 1200px;
    height: 1054px;
    overflow: hidden;
    background: var(--page-bg);
    font-family: "Roboto", Arial, sans-serif;
  }
  .card {
    position: absolute;
    left: 100px;
    top: 241px;
    width: 1000px;
    height: 572px;
    border-radius: 26px;
    background: var(--card-frost);
    border: 2px solid var(--card-edge);
    overflow: hidden;
    box-shadow: 0 12px 30px rgba(0,0,0,0.12);
  }
  .card-panel {
    position: absolute;
    left: 0;
    top: 0;
    width: 1000px;
    height: 572px;
  }
  .brand {
    position: absolute;
    left: 40px;
    top: 286px;
    width: 460px;
    transform-origin: 0 0;
    transform: translate(0, 220px) rotate(-90deg);
    color: var(--white);
    font-weight: 900;
    font-size: 64px;
    line-height: 1;
    letter-spacing: 0.5px;
  }
  .brand-line { display: block; }
  .brand-line + .brand-line { margin-top: 6px; }
  .services {
    position: absolute;
    left: 252px;
    top: 500px;
    transform-origin: 0 0;
    transform: rotate(-90deg);
    color: var(--white);
    font-weight: 700;
    font-size: 22px;
    letter-spacing: 1.5px;
    white-space: nowrap;
  }
  .details {
    position: absolute;
    left: 446px;
    top: 140px;
  }
  .person-name {
    font-weight: 700;
    font-size: 42px;
    color: var(--name-blue);
    letter-spacing: 1px;
    line-height: 1;
  }
  .person-title {
    margin-top: 14px;
    font-size: 24px;
    color: var(--text-dark);
  }
  .call-line {
    margin-top: 72px;
    font-weight: 700;
    font-size: 34px;
    line-height: 1;
    letter-spacing: 0.5px;
  }
  .call-label { color: var(--call-light); }
  .call-number { color: var(--call-navy); }
  .contact-list {
    list-style: none;
    margin-top: 20px;
  }
  .contact-item {
    display: flex;
    align-items: center;
    height: 36px;
    font-size: 24px;
    color: var(--text-dark);
  }
  .contact-icon {
    width: 22px;
    height: 22px;
    margin-right: 22px;
    flex: none;
  }
</style>
</head>
<body>
  <div class="card">
    <svg class="card-panel" viewBox="0 0 1000 572" aria-hidden="true">
      <path d="M0 0 H345 Q420 286 335 572 H0 Z" fill="var(--panel-accent)"/>
      <path d="M0 0 H330 Q404 286 320 572 H0 Z" fill="var(--panel-blue)"/>
      <path d="M0 0 H150 Q200 286 140 572 H0 Z" fill="var(--panel-deep)" opacity="0.35"/>
    </svg>

    <div class="brand">
      <span class="brand-line">Lakeshore</span>
      <span class="brand-line">Bright Wash</span>
    </div>
    <div class="services">COMMERCIAL RESIDENTIAL FLEET</div>

    <div class="details">
      <h1 class="person-name">DANA WHITFIELD</h1>
      <p class="person-title">Managing Director</p>
      <p class="call-line"><span class="call-label">CALL</span> <span class="call-number">855-GLO-TEAM</span></p>
      <ul class="contact-list">
        <li class="contact-item">
          <svg class="contact-icon" viewBox="0 0 24 24" aria-hidden="true">
            <path d="M12 1.5a7.5 7.5 0 0 0-7.5 7.5c0 5.6 7.5 13.5 7.5 13.5s7.5-7.9 7.5-13.5A7.5 7.5 0 0 0 12 1.5z" fill="var(--icon-blue)"/>
            <circle cx="12" cy="9" r="3" fill="var(--card-frost)"/>
          </svg>
          214 Birch Ave. Harbor Point, MI 49101
        </li>
        <li class="contact-item">
          <svg class="contact-icon" viewBox="0 0 24 24" aria-hidden="true">
            <circle cx="12" cy="12" r="10" fill="var(--icon-blue)"/>
            <g fill="none" stroke="var(--card-frost)" stroke-width="1.4">
              <ellipse cx="12" cy="12" rx="4" ry="10"/>
              <line x1="2" y1="12" x2="22" y2="12"/>
              <line x1="4" y1="7" x2="20" y2="7"/>
              <line x1="4" y1="17" x2="20" y2="17"/>
            </g>
          </svg>
          lakeshorebrightwash.example
        </li>
        <li class="contact-item">
          <svg class="contact-icon" viewBox="0 0 24 24" aria-hidden="true">
            <rect x="2" y="5" width="20" height="14" rx="1.5" fill="var(--icon-blue)"/>
            <path d="M2.5 6 L12 13 L21.5 6" fill="none" stroke="var(--card-frost)" stroke-width="1.6"/>
          </svg>
          info@lakeshorebrightwash.example
        </li>
      </ul>
    </div>
  </div>
</body>
</html>
```